Looking for a new business card design

We are looking for a corporate looking yet still a bit different then the rest. I would like the card black with the picture on the back and the phrase "Guiding every crew home safely" on the back as well. Then a clean look on the front with a bit of an edge.

Target Market(s)

Corporate oil executives and drilling supervisors

Industry/Entity Type

Oil And Gas

Contact Information for Business Card

Black, bold, clean lines.

Font styles to use
Sans Serif

Requirements
Must have
• Picture on the back with the slogan "Guiding every crew home safely"
• Black background
• Stands out

```html
<!DOCTYPE html>
<html lang="en">
<head>
<meta charset="utf-8">
<title>Vantor Energy Services Corp. – Business Card</title>
<link rel="stylesheet" href="https://fonts.googleapis.com/css2?family=Open+Sans:wght@300;400;600;700&display=swap">
<style>
  :root {
    --canvas: #e9e6e1;
    --card-white: #f7f7f7;
    --card-white-edge: #e2e2e2;
    --card-black: #262626;
    --lime: #c5d82e;
    --ink: #1c1c1c;
    --grey: #8a8a8a;
    --on-dark: #ededed;
    --on-dark-muted: #c9c9c9;
  }
  * { box-sizing: border-box; margin: 0; padding: 0; }
  html, body { width: 1200px; height: 1023px; overflow: hidden; }
  body {
    background: var(--canvas);
    font-family: "Open Sans", sans-serif;
    position: relative;
  }
  .card {
    position: absolute;
    left: 250px;
    width: 700px;
    height: 400px;
    border-radius: 22px;
    overflow: hidden;
    box-shadow: 0 10px 26px rgba(0,0,0,.18);
  }

  /* Front */
  .card--front {
    top: 70px;
    background: linear-gradient(135deg, #ffffff 0%, var(--card-white) 55%, var(--card-white-edge) 100%);
  }
  .brand {
    position: absolute;
    display: flex;
    align-items: center;
    gap: 16px;
  }
  .brand__dot {
    width: 54px; height: 54px;
    border-radius: 50%;
    background: var(--lime);
    flex: none;
  }
  .brand__name {
    font-weight: 700;
    color: var(--lime);
    line-height: 1;
    letter-spacing: .02em;
  }
  .brand__sub {
    font-weight: 300;
    line-height: 1.2;
  }
  .card--front .brand { left: 50px; top: 70px; }
  .card--front .brand__name { font-size: 48px; }
  .card--front .brand__sub { font-size: 21px; color: var(--grey); }

  .address {
    position: absolute;
    right: 44px;
    top: 44px;
    text-align: right;
    font-size: 15px;
    font-style: normal;
    color: var(--ink);
    line-height: 1.45;
    letter-spacing: .03em;
  }
  .person {
    position: absolute;
    left: 50px;
    top: 205px;
  }
  .person__name {
    font-size: 30px;
    font-weight: 600;
    color: var(--ink);
    line-height: 1.1;
  }
  .person__title {
    font-size: 15px;
    color: var(--lime);
    font-weight: 600;
  }
  .contacts {
    position: absolute;
    left: 50px;
    top: 285px;
    list-style: none;
    font-size: 15px;
    color: var(--ink);
    letter-spacing: .03em;
  }
  .contacts li {
    display: flex;
    align-items: center;
    gap: 12px;
    line-height: 28px;
  }
  .contacts svg { width: 16px; height: 16px; flex: none; }

  /* Back */
  .card--back {
    top: 540px;
    background: var(--card-black);
  }
  .card--back .brand { left: 190px; top: 120px; }
  .card--back .brand__dot { width: 80px; height: 80px; }
  .card--back .brand__name { font-size: 64px; }
  .card--back .brand__sub { font-size: 24px; color: var(--on-dark); }
  .slogan {
    position: absolute;
    left: 0; right: 0;
    top: 290px;
    text-align: center;
    font-size: 21px;
    color: var(--on-dark-muted);
    letter-spacing: .05em;
  }
</style>
</head>
<body>

  <section class="card card--front" aria-label="Business card front">
    <div class="brand">
      <span class="brand__dot" aria-hidden="true"></span>
      <div>
        <div class="brand__name">VANTOR</div>
        <div class="brand__sub">Energy Services Corp.</div>
      </div>
    </div>

    <address class="address">
      Your address line1<br>
      Your address line 2
    </address>

    <div class="person">
      <div class="person__name">Your Name</div>
      <div class="person__title">Title</div>
    </div>

    <ul class="contacts">
      <li>
        <svg viewBox="0 0 16 16" aria-hidden="true"><circle cx="8" cy="8" r="7" fill="none" stroke="#c5d82e" stroke-width="1.4"/><path d="M5.5 4.5l1.5 1.5-1 1.2a5 5 0 0 0 2.8 2.8l1.2-1 1.5 1.5-1 1.2c-3 0-6-3-6-6z" fill="#c5d82e"/></svg>
        88-123-54321
      </li>
      <li>
        <svg viewBox="0 0 16 16" aria-hidden="true"><rect x="1.5" y="3.5" width="13" height="9" fill="none" stroke="#c5d82e" stroke-width="1.3"/><path d="M1.5 3.5L8 9l6.5-5.5" fill="none" stroke="#c5d82e" stroke-width="1.3"/></svg>
        info@yourweb.com
      </li>
      <li>
        <svg viewBox="0 0 16 16" aria-hidden="true"><circle cx="8" cy="8" r="6.5" fill="none" stroke="#c5d82e" stroke-width="1.3"/><ellipse cx="8" cy="8" rx="3" ry="6.5" fill="none" stroke="#c5d82e" stroke-width="1.1"/><path d="M1.5 8h13" stroke="#c5d82e" stroke-width="1.1"/></svg>
        www.yourweb.com
      </li>
    </ul>
  </section>

  <section class="card card--back" aria-label="Business card back">
    <div class="brand">
      <span class="brand__dot" aria-hidden="true"></span>
      <div>
        <div class="brand__name">VANTOR</div>
        <div class="brand__sub">Energy Services Corp.</div>
      </div>
    </div>
    <p class="slogan">Guiding every crew home safely</p>
  </section>

</body>
</html>
```